Global Expert Network Firm needs business card design

We need business card design for a new company based in Seoul, South Korea called 'Corwell Insight Partners'. We recruit industry experts covering all countries and connect our client and recruited expert by phone, face-to-face meetings and etc. We are a global expert network firm that is focused on delivering high-quality experts to our clients throughout the world. Our clients include multinational corporations, global consulting firms, private equity firms, venture capital firms, asset management companies.
We have made new logo and please find attachment.(Please use new logo)
Target Market(s)
Global Consulting Firms, Investment Firms, Private Equity Firms, Venture Capital Firms.
Industry/Entity Type
Recruitment
Contact Information for Business Card
We need two Languages (English and Korean Version).
The front is Korean and the back is English version.
[The back] [English]
Company Name: Corwell Insight Partners, Inc.
CEO Name: Daniel Park
Address: #507, Hanbit Bldg, 82 Maebongsan-ro, Dobong-gu, Seoul, 01327, Korea
Tel. +82 2 718 4052
Fax. +82 2 864 1097
Mobile. +82 10 7264 8815
Email: daniel@corwellip.com
Web: www.corwellip.com
[The front] [Korean] => Described in same order as English version.
회사명: 코웰인사이트파트너스(주)
대표이사: 박도현
주소: 서울시 도봉구 매봉산로 82 한빛빌딩 507호
Tel. 02 718 4052
Fax. 02 864 1097
Mobile. 010 7264 8815
Web: www.corwellip.com
Look and feel
Each slider illustrates characteristics of the customer's brand and the style your logo design should communicate.

```html
<!DOCTYPE html>
<html lang="ko">
<head>
<meta charset="utf-8">
<title>Corwell Insight Partners — Business Cards</title>
<link rel="stylesheet" href="https://fonts.googleapis.com/css2?family=Karla:wght@400;500&family=Noto+Sans+KR:wght@400;500&display=swap">
<style>
  :root {
    --brand-blue: #37478a;
    --paper: #ffffff;
    --ink: #2b2b2b;
    --backdrop: #eceae5;
  }
  * { box-sizing: border-box; margin: 0; padding: 0; }
  html, body {
    width: 1200px; height: 1200px; overflow: hidden;
    background: var(--backdrop);
  }
  .sheet {
    width: 1200px; height: 1200px;
    display: flex; flex-direction: column; align-items: center; justify-content: center;
    gap: 54px;
  }
  .card {
    width: 900px; height: 513px;
    display: flex;
    background: var(--paper);
    box-shadow: 0 2px 10px rgba(0,0,0,0.12);
  }
  .card__brand-panel {
    width: 450px; height: 100%;
    background: var(--brand-blue);
    color: var(--paper);
    position: relative;
    padding: 72px 0 0 50px;
  }
  .brand-mark {
    display: flex; align-items: center; gap: 14px;
  }
  .brand-mark__square {
    width: 18px; height: 18px;
    background: var(--paper);
    flex: none;
  }
  .brand-mark__name {
    font-family: "Karla", sans-serif;
    font-weight: 400;
    font-size: 27px;
    line-height: 1.2;
    color: var(--paper);
  }
  .holder {
    position: absolute; left: 50px; bottom: 48px;
  }
  .holder__name {
    font-family: "Karla", sans-serif;
    font-weight: 500;
    font-size: 31px;
    line-height: 1.2;
  }
  .holder__title {
    font-family: "Karla", sans-serif;
    font-weight: 400;
    font-size: 19px;
    margin-top: 4px;
  }
  .card--ko .holder__name,
  .card--ko .holder__title { font-family: "Noto Sans KR", sans-serif; }
  .card--ko .holder__name { font-size: 32px; }
  .card__details {
    flex: 1;
    padding: 150px 0 0 32px;
    color: var(--ink);
    font-family: "Karla", sans-serif;
  }
  .card--ko .card__details { padding-top: 130px; }
  .company-name {
    display: inline-block;
    font-size: 27px;
    font-weight: 400;
    padding-bottom: 8px;
    border-bottom: 2px solid var(--brand-blue);
    margin-bottom: 20px;
  }
  .card--ko .company-name {
    font-family: "Noto Sans KR", sans-serif;
    font-size: 30px;
  }
  .contact-lines {
    list-style: none;
    font-size: 21px;
    line-height: 31px;
  }
  .address-ko {
    font-family: "Noto Sans KR", sans-serif;
    font-size: 21px;
    line-height: 32px;
    margin-bottom: 14px;
  }
</style>
</head>
<body>
<main class="sheet">

  <section class="card card--ko" aria-label="Korean side">
    <div class="card__brand-panel">
      <div class="brand-mark">
        <span class="brand-mark__square"></span>
        <p class="brand-mark__name">Corwell Insight Partners</p>
      </div>
      <div class="holder">
        <p class="holder__name">박도현</p>
        <p class="holder__title">대표이사</p>
      </div>
    </div>
    <div class="card__details">
      <h1 class="company-name">코웰인사이트파트너스(주)</h1>
      <p class="address-ko">서울시 도봉구 매봉산로<br>82 한빛빌딩 507호</p>
      <ul class="contact-lines">
        <li>Tel. +82 2 718 4052</li>
        <li>Fax. +82 2 864 1097</li>
        <li>Mobile. +82 10 7264 8815</li>
        <li>Email: daniel@corwellip.com</li>
        <li>Web: www.corwellip.com</li>
      </ul>
    </div>
  </section>

  <section class="card card--en" aria-label="English side">
    <div class="card__brand-panel">
      <div class="brand-mark">
        <span class="brand-mark__square"></span>
        <p class="brand-mark__name">Corwell Insight Partners</p>
      </div>
      <div class="holder">
        <p class="holder__name">Daniel Park</p>
        <p class="holder__title">CEO</p>
      </div>
    </div>
    <div class="card__details">
      <h2 class="company-name">Corwell Insight Partners, Inc.</h2>
      <ul class="contact-lines">
        <li>#507, Hanbit Bldg,</li>
        <li>82 Maebongsan-ro,</li>
        <li>Dobong-gu,</li>
        <li>Seoul, 01327, Korea</li>
        <li>Tel. +82 2 718 4052</li>
        <li>Fax. +82 2 864 1097</li>
        <li>Mobile. +82 10 7264 8815</li>
        <li>Email: daniel@corwellip.com</li>
        <li>Web: www.corwellip.com</li>
      </ul>
    </div>
  </section>

</main>
</body>
</html>
```